Bref créative
bussines card and stationary
paper letterhead
Bright & Fun-filled
tavirel cusan
managing partner
14 lunca verde street, sector 3 Bucharest Romania
tavirel@plumvox.com
www.plumvox.com
The card will be printed on the very best paper there is.will use 500g paper to be thick and heavy.
I want when someone recieves the card to feel like - waaaaawww this is top quality business card - the printing,the paper, the attention to details - everyting is just perfect.
The company develiopes software for mobile phones, various applications dedicated to sport industry.The most important one "plumvox" will be rewinding recorded videos from various sports. In all the products launched by this company a LOT of attentions is offered to all the details - so that the final product is extremelly well designed, top quality and extremely reliable.
this is what the card needs to suggest as well - attention to details, professionalism and top quality.
Use the back for adquate graphics, drawings etc .Be creative.Impress!
logo
logo ai

```html
<!DOCTYPE html>
<html lang="en">
<head>
<meta charset="utf-8">
<title>plumvox stationery</title>
<link rel="stylesheet" href="https://fonts.googleapis.com/css2?family=Raleway:wght@300;400;600&display=swap">
<style>
  :root {
    --red: #e5232c;
    --red-soft: #f7d6d7;
    --paper: #ffffff;
    --board: #ededed;
    --dark: #3a3a3c;
    --ink: #5a5a5a;
    --muted: #9a9a9a;
    --flap-dark: #242424;
    --shadow: 0 2px 5px rgba(0,0,0,.22);
  }
  * { box-sizing: border-box; margin: 0; padding: 0; }
  html, body { width: 1200px; height: 310px; overflow: hidden; }
  body { background: var(--board); font-family: "Raleway", sans-serif; color: var(--ink); position: relative; }

  .piece { position: absolute; background: var(--paper); box-shadow: var(--shadow); overflow: hidden; }

  .brand { display: flex; align-items: center; gap: 4px; white-space: nowrap; }
  .brand-dot { border-radius: 50%; background: var(--red); flex: none; }
  .brand-name { font-weight: 400; color: var(--red); letter-spacing: .02em; line-height: 1; }
  .brand.on-red .brand-dot { background: var(--paper); }
  .brand.on-red .brand-name { color: var(--paper); }

  /* identity block */
  .identity { position: absolute; left: 20px; top: 14px; width: 120px; }
  .identity .mark { width: 38px; height: 38px; border-radius: 50%; background: var(--red); margin: 0 0 24px 22px; }
  .identity .name { font-size: 22px; font-weight: 300; color: var(--dark); line-height: 1; }
  .identity .tagline { font-size: 7px; color: var(--ink); margin-top: 5px; letter-spacing: .05em; }

  /* cards */
  .card-front { left: 17px; top: 150px; width: 108px; height: 66px; }
  .card-front .band { position: absolute; left: 0; right: 0; top: 0; height: 13px; background: var(--red); }
  .card-front .brand { position: absolute; left: 6px; top: 20px; }
  .card-front .person { position: absolute; left: 6px; top: 33px; right: 4px; font-size: 4.5px; line-height: 1.55; white-space: nowrap; }
  .card-front .person .person-name { font-weight: 600; color: var(--dark); font-size: 5px; }

  .card-back-white { left: 17px; top: 233px; width: 108px; height: 60px; }
  .card-back-red { left: 132px; top: 233px; width: 103px; height: 60px; background: var(--red); }
  .card-back-white .brand, .card-back-red .brand { position: absolute; left: 50%; top: 50%; transform: translate(-50%,-50%); }
  .card-back-white .web { position: absolute; bottom: 5px; width: 100%; text-align: center; font-size: 3.5px; color: var(--muted); }

  /* letterheads */
  .letterhead { top: 7px; width: 194px; height: 276px; }
  .letterhead.one { left: 271px; }
  .letterhead.two { left: 490px; }
  .letterhead .band { position: absolute; left: 0; right: 0; top: 10px; height: 18px; background: var(--red); }
  .letterhead .badge { position: absolute; left: 14px; top: 4px; width: 30px; height: 30px; border-radius: 50%; background: var(--paper); border: 3px solid var(--red); }
  .letterhead .brand { position: absolute; left: 12px; top: 39px; }
  .watermark { position: absolute; left: 50%; top: 95px; transform: translateX(-50%); display: flex; flex-direction: column; align-items: center; gap: 6px; }
  .watermark .ring { width: 78px; height: 78px; border-radius: 50%; background: var(--red-soft); opacity: .6; }
  .watermark .word { font-size: 14px; color: var(--red-soft); font-weight: 300; }
  .letterhead .foot { position: absolute; bottom: 7px; width: 100%; text-align: center; font-size: 3.5px; color: var(--muted); white-space: nowrap; }

  /* small envelopes */
  .envelope { left: 698px; width: 190px; height: 108px; }
  .envelope.upper { top: 7px; }
  .envelope.lower { top: 175px; }
  .envelope .band { position: absolute; left: 0; right: 0; top: 8px; height: 14px; background: var(--red); }
  .envelope .badge { position: absolute; left: 12px; top: 3px; width: 24px; height: 24px; border-radius: 50%; background: var(--paper); border: 3px solid var(--red); }
  .envelope .brand { position: absolute; left: 10px; top: 30px; }
  .envelope .foot { position: absolute; bottom: 6px; width: 100%; text-align: center; font-size: 3.5px; color: var(--muted); }

  /* dark presentation panel */
  .panel { position: absolute; left: 907px; top: 0; width: 293px; height: 310px; background: var(--dark); }
  .panel svg { position: absolute; left: 0; top: 0; }
</style>
</head>
<body>

<section class="identity">
  <div class="mark"></div>
  <div class="name">plumvox</div>
  <div class="tagline">Sport Video Replay</div>
</section>

<article class="piece card-front">
  <div class="band"></div>
  <div class="brand"><span class="brand-dot" style="width:7px;height:7px"></span><span class="brand-name" style="font-size:7px">plumvox</span></div>
  <div class="person">
    <span class="person-name">tavirel cusan</span><br>
    managing partner<br>
    14 lunca verde street, sector 3<br>
    tavirel@plumvox.com
  </div>
</article>

<article class="piece card-back-white">
  <div class="brand"><span class="brand-dot" style="width:9px;height:9px"></span><span class="brand-name" style="font-size:10px">plumvox</span></div>
  <div class="web">www.plumvox.com</div>
</article>

<article class="piece card-back-red">
  <div class="brand on-red"><span class="brand-dot" style="width:9px;height:9px"></span><span class="brand-name" style="font-size:10px">plumvox</span></div>
</article>

<article class="piece letterhead one">
  <div class="band"></div>
  <div class="badge"></div>
  <div class="brand"><span class="brand-name" style="font-size:6px">plumvox</span></div>
  <div class="watermark" role="img" aria-label="faint brand emblem"><div class="ring"></div><div class="word">plumvox</div></div>
  <div class="foot">14 lunca verde street, sector 3 · Bucharest Romania · www.plumvox.com</div>
</article>

<article class="piece letterhead two">
  <div class="band"></div>
  <div class="badge"></div>
  <div class="brand"><span class="brand-name" style="font-size:6px">plumvox</span></div>
  <div class="watermark" role="img" aria-label="faint brand emblem"><div class="ring"></div><div class="word">plumvox</div></div>
  <div class="foot">14 lunca verde street, sector 3 · Bucharest Romania · www.plumvox.com</div>
</article>

<article class="piece envelope upper">
  <div class="band"></div>
  <div class="badge"></div>
  <div class="brand"><span class="brand-name" style="font-size:5px">plumvox</span></div>
  <div class="foot">www.plumvox.com</div>
</article>

<article class="piece envelope lower">
  <div class="band"></div>
  <div class="badge"></div>
  <div class="brand"><span class="brand-name" style="font-size:5px">plumvox</span></div>
  <div class="foot">www.plumvox.com</div>
</article>

<aside class="panel">
  <svg width="293" height="310" viewBox="0 0 293 310" role="img" aria-label="envelope backs">
    <g class="env-back-dark">
      <rect x="40" y="22" width="240" height="90" fill="#ffffff"/>
      <polygon points="40,22 280,22 160,78" fill="var(--flap-dark)"/>
      <circle cx="160" cy="70" r="9" fill="var(--red)"/>
    </g>
    <g class="env-back-red">
      <rect x="28" y="112" width="250" height="82" fill="#ffffff"/>
      <polygon points="28,112 278,112 153,165" fill="var(--red)"/>
      <circle cx="153" cy="158" r="8" fill="var(--paper)"/>
    </g>
    <g class="env-back-white">
      <rect x="22" y="200" width="256" height="88" fill="#ffffff"/>
      <polyline points="22,200 150,250 278,200" fill="none" stroke="#cccccc" stroke-width="1"/>
      <line x1="22" y1="288" x2="120" y2="238" stroke="#e3e3e3" stroke-width="1"/>
      <line x1="278" y1="288" x2="180" y2="238" stroke="#e3e3e3" stroke-width="1"/>
      <circle cx="150" cy="248" r="7" fill="var(--red)"/>
    </g>
  </svg>
</aside>

</body>
</html>
```